VelnoraTek Bright IT Consultancy
All Stationary + ESignaure + Powerpoint Template
Simple
Tomás Barrena Ollé
President & CEO
3er Cjon Calle Fresal 57
Las Brisas, Coyoacán
México DF, 07215
See additional comments
tomas.barrena@velnoratek.mx
www.velnoratek.com.mx
I dont have a permanent local phone number yet, so I dont want to give an informal impression about the company, so Designers I need your creativite to avoid that impression something as simple as "cell&phone" but with all your experience and creativity, an special cell+phone logo for example. Other request is a clean, simple, modern, corporate and professional material.
Go Bright...Go Sky
Go Sky...& Connect
Share...& Succed
Logo Velno
Logo Velno 2
Logo 3
Logo 4
This is an example of standard bullets and numbers in a powerpoint presentation

```html
<!DOCTYPE html>
<html lang="en">
<head>
<meta charset="utf-8">
<title>VelnoraTek Presentation Template</title>
<link rel="stylesheet" href="https://fonts.googleapis.com/css2?family=Open+Sans:ital,wght@0,400;0,600;0,700;1,600&display=swap">
<style>
  :root {
    --stage: #a4a4a4;
    --slide: #ffffff;
    --slide-shade: #eceef0;
    --brand-blue: #3d6a88;
    --olive: #8b9a3b;
    --ink: #6d6d6d;
    --ink-soft: #9a9a9a;
    --rule: #d7dbde;
    --pie-dark: #5b5f63;
    --pie-light: #a9adb1;
  }
  * { box-sizing: border-box; margin: 0; padding: 0; }
  html, body { width: 1200px; height: 876px; overflow: hidden; }
  body {
    background: var(--stage);
    font-family: "Open Sans", Arial, sans-serif;
    position: relative;
  }
  .slide {
    position: absolute;
    width: 326px;
    height: 240px;
    background: linear-gradient(180deg, var(--slide) 0%, var(--slide) 55%, var(--slide-shade) 100%);
    box-shadow: 0 1px 3px rgba(0,0,0,.25);
    overflow: hidden;
  }
  .title-slide { left: 259px; top: 53px; }
  .thanks-slide { left: 610px; top: 53px; }
  .groups-slide { left: 77px; top: 319px; }
  .pie-slide { left: 432px; top: 319px; }
  .welcome-slide { left: 787px; top: 319px; }
  .picture-slide { left: 77px; top: 583px; }
  .bars-slide { left: 432px; top: 583px; }
  .agenda-slide { left: 787px; top: 583px; }

  .brand {
    position: absolute;
    display: flex;
    align-items: center;
    gap: 7px;
    color: var(--brand-blue);
    font-weight: 600;
    font-size: 27px;
    letter-spacing: -0.5px;
  }
  .brand-square { width: 26px; height: 26px; background: var(--brand-blue); }
  .title-slide .brand { left: 16px; top: 24px; }
  .thanks-slide .brand { left: 16px; top: 30px; }

  .title-decoration {
    position: absolute;
    left: 138px; top: 58px;
    width: 150px; height: 160px;
    border-radius: 20px;
    background: radial-gradient(circle at 50% 45%, rgba(176,186,150,.45), rgba(190,202,210,.3) 55%, rgba(255,255,255,0) 75%);
  }
  .welcome-line { position: absolute; left: 16px; top: 144px; color: var(--olive); font-size: 15px; }
  .presentation-name { position: absolute; left: 16px; top: 163px; color: var(--brand-blue); font-size: 19px; font-weight: 700; }
  .description { position: absolute; left: 16px; top: 189px; color: var(--ink); font-size: 12px; }
  .thanks { position: absolute; left: 16px; top: 140px; color: var(--brand-blue); font-size: 26px; font-weight: 700; }
  .for-coming { position: absolute; left: 16px; top: 176px; color: var(--brand-blue); font-size: 14px; }

  .heading { position: absolute; left: 14px; top: 12px; color: var(--brand-blue); font-size: 14px; font-weight: 700; }
  .subheading { position: absolute; left: 14px; top: 32px; color: var(--ink); font-size: 8px; }
  .small-text { color: var(--ink-soft); font-size: 4.6px; line-height: 1.45; }

  .group { position: absolute; width: 132px; }
  .group-title { color: var(--brand-blue); font-size: 6px; font-weight: 700; margin-bottom: 1px; }
  .g1 { left: 14px; top: 62px; }
  .g2 { left: 168px; top: 62px; }
  .g3 { left: 14px; top: 138px; }
  .g4 { left: 168px; top: 138px; }

  .pie { position: absolute; left: 26px; top: 78px; }
  .pie-copy { position: absolute; left: 148px; top: 100px; width: 140px; }

  .band {
    position: absolute; left: 0; top: 0; width: 100%; height: 40px;
    background: linear-gradient(180deg, #f6f7f8, #e6e9eb);
    border-bottom: 1px solid var(--rule);
  }
  .band-title { position: absolute; left: 16px; top: 11px; color: var(--brand-blue); font-size: 12px; font-weight: 600; font-style: italic; }
  .point-list { position: absolute; left: 18px; top: 62px; list-style: none; width: 290px; }
  .point-list li { display: flex; gap: 8px; margin-bottom: 14px; color: var(--ink); font-size: 6px; line-height: 1.5; }
  .point-icon { flex: none; width: 12px; height: 12px; }

  .picture-box {
    position: absolute; left: 14px; top: 68px; width: 90px; height: 100px;
    border: 1px solid #b9bdc0; border-radius: 6px;
    background: linear-gradient(180deg, #f8f8f8, #d9dcde);
    display: flex; align-items: center; justify-content: center; text-align: center;
    color: #444; font-size: 8.5px; font-weight: 700; line-height: 1.3;
    box-shadow: 0 1px 2px rgba(0,0,0,.2);
  }
  .picture-copy { position: absolute; left: 122px; top: 72px; width: 150px; }
  .bars-copy { position: absolute; left: 16px; top: 100px; width: 130px; }
  .bars { position: absolute; left: 186px; top: 80px; }

  .agenda-list { position: absolute; left: 28px; top: 58px; list-style: none; }
  .agenda-list li { display: flex; align-items: center; gap: 6px; color: var(--ink-soft); font-size: 5px; height: 14px; }
  .agenda-list li.sub { padding-left: 14px; }
  .agenda-list li.gap { margin-top: 12px; }
  .agenda-dot { width: 5px; height: 5px; border-radius: 50%; background: var(--brand-blue); }
  .sub .agenda-dot { background: var(--pie-light); }
</style>
</head>
<body>

<section class="slide title-slide">
  <div class="brand"><span class="brand-square"></span>VelnoraTek</div>
  <div class="title-decoration" role="img" aria-label="Faint decorative brand pattern area"></div>
  <p class="welcome-line">Welcome to Our</p>
  <p class="presentation-name">Presentation Name</p>
  <p class="description">Description</p>
</section>

<section class="slide thanks-slide">
  <div class="brand"><span class="brand-square"></span>VelnoraTek</div>
  <p class="thanks">Thanks</p>
  <p class="for-coming">For Coming</p>
</section>

<section class="slide groups-slide">
  <h2 class="heading">Heading Here</h2>
  <p class="subheading">Sub Heading Here</p>
  <div class="group g1"><p class="group-title">Group 1</p><p class="small-text">Lorem ipsum is simply dummy text of the printing and typesetting industry. Lorem ipsum has been the industry standard dummy text ever since the 1500s, when an unknown printer took a galley of type.</p></div>
  <div class="group g2"><p class="group-title">Group 3</p><p class="small-text">Lorem ipsum is simply dummy text of the printing and typesetting industry. Lorem ipsum has been the industry standard dummy text ever since the 1500s, when an unknown printer took a galley of type.</p></div>
  <div class="group g3"><p class="group-title">Group 2</p><p class="small-text">Lorem ipsum is simply dummy text of the printing and typesetting industry. Lorem ipsum has been the industry standard dummy text ever since the 1500s, when an unknown printer took a galley of type.</p></div>
  <div class="group g4"><p class="group-title">Group 4</p><p class="small-text">Lorem ipsum is simply dummy text of the printing and typesetting industry. Lorem ipsum has been the industry standard dummy text ever since the 1500s, when an unknown printer took a galley of type.</p></div>
</section>

<section class="slide pie-slide">
  <h2 class="heading">Heading Here</h2>
  <p class="subheading">Sub Heading Here</p>
  <svg class="pie" width="100" height="100" viewBox="0 0 100 100" aria-hidden="true">
    <path d="M50 50 L50 5 A45 45 0 1 1 23.5 86.4 Z" fill="var(--brand-blue)"/>
    <path d="M50 50 L23.5 86.4 A45 45 0 0 1 7.2 36.1 Z" fill="var(--pie-dark)"/>
    <path d="M50 50 L7.2 36.1 A45 45 0 0 1 50 5 Z" fill="var(--pie-light)"/>
  </svg>
  <p class="pie-copy small-text">Lorem ipsum is simply dummy text of the printing and typesetting industry. Lorem ipsum has been the industry standard dummy text ever since the 1500s, when an unknown printer took a galley of type.</p>
</section>

<section class="slide welcome-slide">
  <div class="band"></div>
  <h2 class="band-title">Welcome to our Presentation</h2>
  <ul class="point-list">
    <li><svg class="point-icon" viewBox="0 0 12 12" aria-hidden="true"><circle cx="6" cy="6" r="5.5" fill="var(--brand-blue)"/><path d="M5 3.5 L7.5 6 L5 8.5" stroke="#fff" stroke-width="1.3" fill="none"/></svg><span>This is a sample text.. So design your layout for presentation Project.</span></li>
    <li><svg class="point-icon" viewBox="0 0 12 12" aria-hidden="true"><circle cx="6" cy="6" r="5.5" fill="var(--brand-blue)"/><path d="M5 3.5 L7.5 6 L5 8.5" stroke="#fff" stroke-width="1.3" fill="none"/></svg><span>This is a sample text.. So design your layout for presentation Project.</span></li>
    <li><svg class="point-icon" viewBox="0 0 12 12" aria-hidden="true"><circle cx="6" cy="6" r="5.5" fill="var(--brand-blue)"/><path d="M5 3.5 L7.5 6 L5 8.5" stroke="#fff" stroke-width="1.3" fill="none"/></svg><span>This is a sample text.. So design your layout for presentation Project.</span></li>
  </ul>
</section>

<section class="slide picture-slide">
  <h2 class="heading">Heading Here</h2>
  <p class="subheading">Sub Heading Here</p>
  <div class="picture-box">Insert Picture<br>Here</div>
  <p class="picture-copy small-text">Lorem ipsum is simply dummy text of the printing and typesetting industry. Lorem ipsum has been the industry standard dummy text ever since the 1500s, when an unknown printer took a galley of type.</p>
</section>

<section class="slide bars-slide">
  <h2 class="heading">Heading Here</h2>
  <p class="subheading">Sub Heading Here</p>
  <p class="bars-copy small-text">Lorem ipsum is simply dummy text of the printing and typesetting industry. Lorem ipsum has been the industry standard dummy text ever since the 1500s, when an unknown printer took a galley of type.</p>
  <svg class="bars" width="110" height="110" viewBox="0 0 110 110" aria-hidden="true">
    <rect x="4" y="52" width="14" height="56" fill="var(--brand-blue)"/>
    <rect x="25" y="20" width="14" height="88" fill="var(--brand-blue)"/>
    <rect x="46" y="44" width="14" height="64" fill="var(--brand-blue)"/>
    <rect x="67" y="34" width="14" height="74" fill="var(--brand-blue)"/>
    <rect x="88" y="28" width="14" height="80" fill="var(--brand-blue)"/>
    <line x1="0" y1="108.5" x2="108" y2="108.5" stroke="var(--rule)"/>
  </svg>
</section>

<section class="slide agenda-slide">
  <div class="band"></div>
  <h2 class="band-title">Agenda</h2>
  <ul class="agenda-list">
    <li><span class="agenda-dot"></span>Lorem ipsum is simply dummy text</li>
    <li><span class="agenda-dot"></span>Lorem ipsum is simply dummy text</li>
    <li><span class="agenda-dot"></span>Lorem ipsum is simply dummy text</li>
    <li class="sub"><span class="agenda-dot"></span>Lorem ipsum is simply dummy text</li>
    <li class="sub"><span class="agenda-dot"></span>Lorem ipsum is simply dummy text</li>
    <li class="gap"><span class="agenda-dot"></span>Lorem ipsum is simply dummy text</li>
    <li class="sub"><span class="agenda-dot"></span>Lorem ipsum is simply dummy text</li>
  </ul>
</section>

</body>
</html>
```